Stationery Design Project

See the detainl of the Basic company project I also have live: http://jobs.briefmarlo.com/job.aspx?id=382917

Reason: I am waiting to select a logo design and ideally the stationery will be from the same person

Industry/Entity Type

It Company

```html
<!DOCTYPE html>
<html lang="en">
<head>
<meta charset="utf-8">
<title>Velantis LLP Letterhead</title>
<link rel="stylesheet" href="https://fonts.googleapis.com/css2?family=Didact+Gothic&display=swap">
<style>
  :root {
    --ink-blue: #1f26e6;
    --leaf-cyan: #2fe3ef;
    --paper: #ffffff;
    --frame: #1a1a1a;
  }
  html, body {
    margin: 0;
    padding: 0;
    width: 860px;
    height: 1200px;
    overflow: hidden;
    background: var(--paper);
  }
  .letterhead {
    position: relative;
    width: 860px;
    height: 1200px;
    font-family: "Didact Gothic", "Century Gothic", sans-serif;
  }
  .sheet-frame {
    position: absolute;
    left: 19px;
    top: 19px;
    width: 821px;
    height: 1160px;
    border: 1.5px solid var(--frame);
    box-sizing: border-box;
  }
  .brand {
    position: absolute;
    left: 112px;
    top: 108px;
    display: flex;
    align-items: center;
    gap: 12px;
    padding-bottom: 4px;
    border-bottom: 1.5px solid var(--leaf-cyan);
  }
  .brand-dot {
    width: 26px;
    height: 26px;
    border-radius: 50%;
    background: var(--leaf-cyan);
  }
  .brand-name {
    margin: 0;
    font-size: 29px;
    font-weight: 400;
    color: var(--ink-blue);
    line-height: 1.1;
    letter-spacing: 0.3px;
  }
  .registered-details {
    position: absolute;
    left: 0;
    right: 0;
    top: 1084px;
    margin: 0;
    text-align: center;
    font-size: 10.5px;
    line-height: 14px;
    color: var(--ink-blue);
    font-style: normal;
    letter-spacing: 0.4px;
    font-weight: 400;
    -webkit-text-stroke: 0.3px var(--ink-blue);
  }
</style>
</head>
<body>
  <main class="letterhead">
    <div class="sheet-frame"></div>

    <header class="brand">
      <span class="brand-dot" aria-hidden="true"></span>
      <h1 class="brand-name">Velantis LLP</h1>
    </header>

    <address class="registered-details">
      Registered Office: Alder House,<br>
      7B Harrowfield Rd, Norbury NB4 2QT<br>
      Partnership No. OC482716
    </address>
  </main>
</body>
</html>
```